4Star Hotel looking for web design

Hello everyone,
We are located in Cambodia, the hotel should open in 2-3 months. The name will be Velmora-Boutique Hotel. We are looking for a webdesign which is professional, elegant and SIMPLE.
All informations should be easy to find. We are quite open to proposition but we would like to the home page:
-a carousel with around 5-8 picture
-Little menu where we can book a room
By the way, we would like a page for our restaurant, gallery, contact page for description of the rooms. I add some old pictures.
I give an example of what we are expecting:
www.quenrostays.com/tovelspring
We hope that we are proposing a good job for you guys. Have fun and Thanks.
Oh and the winner ( or someone he had choose) of course have free night in our presidential suite
Target Market(s)
We are looking for european Market. Let s say people middle age who are willing to travel in difficult area
Industry/Entity Type
Hotel
Coding
Coded - Design and coding required
Number of Pages Required
5+ page
Requirements
Must have
- Simple, simple and Simple
- Carousel
- place for book a room
- during booking, a menu for select room , and after that another menu for propose like tour in town, taxi, flower, bottle of champagne for example
- during all the process, the customer should be able to know at what step it is and can stop and come back after
- Have to be perfect for smartphone
- Price with drawbar for they know how much they earn with our reduction
Nice to have
- during the process of information (name, adress, tel...), it would be great if they can fill it with a button facebook, google plus, lindkdin, instagram ....
- then a button share on facebook, twitter for know that they book in our hotel
- At the end of the booking, a flashcode with the recapitulatif that customer can scan.

```html
<!DOCTYPE html>
<html lang="en">
<head>
<meta charset="UTF-8">
<title>Velmora Boutique Hotel</title>
<link href="https://fonts.googleapis.com/css2?family=Open+Sans:wght@300;400;600;700&family=Raleway:wght@300;400&display=swap" rel="stylesheet">
<style>
:root{
  --teal:#2cbf9d;
  --teal-dark:#24a887;
  --ink:#3b3b3b;
  --muted:#8d8d8d;
  --footer:#2a2a2a;
  --nav:rgba(20,16,12,.72);
  --white:#ffffff;
  --field:#f3f3f3;
}
*{margin:0;padding:0;box-sizing:border-box}
html,body{width:870px;height:1200px;overflow:hidden;background:var(--white);font-family:"Open Sans",Arial,sans-serif;color:var(--ink)}
.page{position:relative;width:870px;height:1200px}

.hero{position:absolute;left:0;top:0;width:870px;height:440px;
  background:radial-gradient(circle at 80% 30%,#f7c36a 0,#d9813a 12%,rgba(120,70,40,.0) 35%),
  linear-gradient(180deg,#3a4a5c 0%,#7b6a5a 35%,#8a5a38 65%,#3d2a1c 100%)}
.hero-carving{position:absolute;left:0;top:0;width:210px;height:440px;background:linear-gradient(90deg,#4a3526,#7a5a3e 70%,rgba(122,90,62,0))}

.nav{position:absolute;left:0;top:0;width:870px;height:36px;background:var(--nav);display:flex;align-items:center;padding:0 24px;font-size:10px;color:var(--white)}
.nav-main{display:flex;gap:16px}
.nav-main a{color:var(--white);text-decoration:none}
.nav-main a.active{color:var(--teal)}
.nav-util{margin-left:auto;display:flex;gap:10px;align-items:center}
.dot{width:14px;height:14px;border-radius:50%;background:#cfcfcf;display:inline-block}

.brand{position:absolute;left:355px;top:130px;width:160px;height:160px;border-radius:50%;background:rgba(255,255,255,.82);display:flex;align-items:center;justify-content:center;text-align:center;font-family:"Raleway",sans-serif;font-size:17px;font-weight:400;color:#4a4a4a;line-height:1.3;padding:20px}

.booking{position:absolute;left:105px;top:360px;width:660px;height:80px;background:var(--white);padding:12px 18px}
.booking-head{display:flex;font-size:9px;color:var(--muted)}
.booking-head b{color:var(--teal);font-weight:400}
.booking-head .adv{margin-left:auto;color:var(--teal)}
.booking-row{display:flex;gap:10px;margin-top:12px}
.field{height:26px;background:var(--field);font-size:9px;color:var(--muted);display:flex;align-items:center;padding:0 8px;width:102px}
.btn-book{height:26px;width:90px;background:var(--teal);color:var(--white);font-size:9px;display:flex;align-items:center;justify-content:center;letter-spacing:.5px}

.offers-title{position:absolute;top:565px;width:870px;text-align:center;font-family:"Raleway",sans-serif;font-weight:300;font-size:22px;letter-spacing:4px}
.offers-sub{position:absolute;top:598px;left:235px;width:400px;text-align:center;font-size:9px;color:var(--muted);line-height:1.5}

.grid{position:absolute;top:645px;left:0;width:870px;height:436px}
.tile{position:absolute}
.photo-room1{left:0;top:0;width:218px;height:218px;background:linear-gradient(160deg,#c9b8a0,#6e5a44)}
.offer{left:218px;top:0;width:218px;height:218px;background:var(--teal);color:var(--white);padding:22px 18px}
.offer h3{font-size:10px;font-weight:600;letter-spacing:1px}
.offer .price{position:absolute;right:18px;top:18px;font-size:17px}
.offer p{font-size:9px;margin-top:14px;line-height:1.5;opacity:.9}
.offer .more{position:absolute;bottom:18px;left:0;width:100%;text-align:center;font-size:9px;letter-spacing:1px}
.photo-room2{left:436px;top:0;width:217px;height:218px;background:linear-gradient(160deg,#4a3a30,#8c6a48 60%,#2a2420)}
.photo-lounge{left:653px;top:0;width:217px;height:218px;background:linear-gradient(160deg,#3a4e8c,#c04a9a 55%,#2a2040)}
.photo-lobby{left:0;top:218px;width:203px;height:218px;background:linear-gradient(160deg,#1e1e1e,#6b6258 60%,#2a2a2a)}
.photo-room3{left:203px;top:218px;width:233px;height:218px;background:linear-gradient(160deg,#b89a72,#e8dcc8 55%,#5a4634)}
.photo-room4{left:436px;top:218px;width:217px;height:218px;background:linear-gradient(160deg,#8a6a52,#e2d6c6 55%,#6a3c30)}
.photo-pool{left:653px;top:218px;width:217px;height:218px;background:linear-gradient(180deg,#5aa0d8 0%,#8ec4e8 45%,#3a5a3a 60%,#2cb8c8 80%)}

.signup{position:absolute;top:1081px;left:0;width:870px;height:80px;background:var(--teal);display:flex;align-items:center;padding:0 215px}
.signup p{font-size:9px;color:var(--white);line-height:1.5;width:290px}
.signup .btn{margin-left:auto;width:110px;height:28px;border:1px solid rgba(255,255,255,.7);background:var(--teal-dark);color:var(--white);font-size:9px;display:flex;align-items:center;justify-content:center}

.footer{position:absolute;top:1161px;left:0;width:870px;height:39px;background:var(--footer);display:flex;align-items:center;padding:0 24px;font-size:9px;color:#cfcfcf}
.footer .util{margin-left:auto;display:flex;gap:10px;align-items:center}
</style>
</head>
<body>
<div class="page">
  <section class="hero" role="img" aria-label="Temple ruins and carved stone figure at sunset">
    <div class="hero-carving"></div>
  </section>

  <nav class="nav">
    <div class="nav-main">
      <a class="active">Home</a><a>Accommodation</a><a>Restaurant &amp; Bar</a><a>Meeting &amp; Events</a><a>Spa</a><a>Special packages</a>
    </div>
    <div class="nav-util"><span>Contact</span><span>|</span><span>Careers</span><span>|</span><span>Follow Us</span><span class="dot"></span><span class="dot"></span><span class="dot"></span></div>
  </nav>

  <div class="brand">Velmora Boutique Hotel</div>

  <form class="booking">
    <div class="booking-head"><span>Fill the form to book now in <b>Velmora Boutique Hotel</b></span><span class="adv">Advanced Search</span></div>
    <div class="booking-row">
      <div class="field">Check in</div>
      <div class="field">Check out</div>
      <div class="field">Adults</div>
      <div class="field">Children</div>
      <div class="field">Promo code</div>
      <div class="btn-book">BOOK NOW</div>
    </div>
  </form>

  <h2 class="offers-title">SPECIAL OFFERS</h2>
  <p class="offers-sub">Discover our seasonal packages and stay longer for less, with breakfast, transfers and guided tours of the old town included in every rate.</p>

  <div class="grid">
    <div class="tile photo-room1" role="img" aria-label="Guest bedroom with double bed"></div>
    <div class="tile offer">
      <h3>WINTER ESCAPE 2015</h3>
      <span class="price">$150</span>
      <p>Three nights in a deluxe room with daily breakfast, airport taxi and a sunset temple tour.</p>
      <span class="more">DETAILS</span>
    </div>
    <div class="tile photo-room2" role="img" aria-label="Hotel suite with warm evening lighting"></div>
    <div class="tile photo-lounge" role="img" aria-label="Lounge bar with pink and blue lighting"></div>
    <div class="tile photo-lobby" role="img" aria-label="Dark hotel lobby with chandelier"></div>
    <div class="tile photo-room3" role="img" aria-label="Bright bedroom with large bed"></div>
    <div class="tile photo-room4" role="img" aria-label="Twin bedroom with white linen"></div>
    <div class="tile photo-pool" role="img" aria-label="Pool terrace overlooking mountains and sea"></div>
  </div>

  <section class="signup">
    <p>Join our newsletter to receive exclusive rates, seasonal offers and news from the hotel before anyone else.</p>
    <div class="btn">SUBSCRIBE</div>
  </section>

  <footer class="footer">
    <span>© 2015 Velmora Boutique Hotel</span>
    <div class="util"><span>Contact</span><span>|</span><span>Careers</span><span>|</span><span>Follow Us</span><span class="dot"></span><span class="dot"></span><span class="dot"></span></div>
  </footer>
</div>
</body>
</html>
```